Wedding invitation

We need a wedding invitation designed with a logo using our initials and name underneath.
We are getting married at THE BRENNA hotel in Gstaad and we would like have our logo similar to theirs but incorporating our initials n&g (any font/case) and our names below noreen and Gilberto. THE BRENNA logo can be seen on their website.
The invitation would be square with the logo on the front in stamped foil and the colour would be THE BRENNA brown (I have the exact colour)
THE BRENNA Brown: C45 M70 Y68 K77
THE BRENNA Rose Gold: VELMAR 218
Inside we would have the invitation wording and on the opposite side some contact info. There would be four inserts - accom, directions, brunch and RSVP. We will provide the wording.

```html
<!DOCTYPE html>
<html lang="en">
<head>
<meta charset="utf-8">
<title>Wedding Invitation – Noreen and Gilberto</title>
<link rel="stylesheet" href="https://fonts.googleapis.com/css2?family=Arimo:wght@400&family=Pinyon+Script&display=swap">
<style>
  :root {
    --page: #ffffff;
    --card: #a6736a;
    --ink: #3a1a14;
    --rose-gold: #dcb9ac;
  }
  html, body {
    margin: 0;
    padding: 0;
    width: 1200px;
    height: 1200px;
    overflow: hidden;
    background: var(--page);
  }
  .invitation {
    position: absolute;
    left: 43px;
    top: 43px;
    width: 1107px;
    height: 1107px;
    background: var(--card);
    color: var(--ink);
    font-family: "Arimo", Arial, sans-serif;
    text-align: center;
  }
  .crest-rule {
    position: absolute;
    left: 296px;
    top: 138px;
    width: 514px;
    height: 12px;
  }
  .crest-ornament {
    position: absolute;
    left: 400px;
    top: 42px;
    width: 320px;
    height: 112px;
    border-radius: 50% 50% 12px 12px / 70% 70% 12px 12px;
    background: radial-gradient(ellipse at 50% 60%, rgba(220,185,172,0.45), rgba(220,185,172,0.12) 70%, rgba(220,185,172,0));
  }
  .wording {
    position: absolute;
    left: 0;
    width: 100%;
    margin: 0;
    font-size: 25px;
    line-height: 50.6px;
    letter-spacing: 1px;
    text-transform: uppercase;
  }
  .wording span { display: block; }
  .wording--hosts { top: 168px; }
  .wording--details { top: 770px; }
  .couple-name {
    position: absolute;
    left: 0;
    width: 100%;
    margin: 0;
    font-family: "Pinyon Script", cursive;
    font-weight: 400;
    font-size: 80px;
    line-height: 1;
  }
  .couple-name--first { top: 521px; }
  .couple-name--second { top: 658px; }
  .couple-joiner {
    position: absolute;
    left: 0;
    width: 100%;
    top: 614px;
    margin: 0;
    font-size: 25px;
    letter-spacing: 1px;
    line-height: 1;
  }
</style>
</head>
<body>
  <main class="invitation">
    <svg class="crest-rule" viewBox="0 0 514 12" aria-hidden="true">
      <path d="M0 6 Q130 3 257 3 Q384 3 514 6 Q384 8 257 8 Q130 8 0 6 Z" fill="var(--rose-gold)"/>
    </svg>
    <div class="crest-ornament" role="img" aria-label="Rose gold calligraphic flourish crest"></div>

    <p class="wording wording--hosts">
      <span>Mr. &amp; Mrs.</span>
      <span>Harold Jennings</span>
      <span>Request you join</span>
      <span>with friends and family</span>
      <span>in the marriage of</span>
      <span>their children</span>
    </p>

    <h1 class="couple-name couple-name--first">Noreen</h1>
    <p class="couple-joiner">AND</p>
    <h1 class="couple-name couple-name--second">Gilberto</h1>

    <p class="wording wording--details">
      <span>On the chosen date of</span>
      <span>Friday the 21st of June, 2014</span>
      <span>at the</span>
      <span>‘The Brenna Gstaad’</span>
      <span>Switzerland</span>
    </p>
  </main>
</body>
</html>
```